Cleaning and Restoration Firm requires a Monthly Newsletter

I would like to begin a monthly newsletter. We have done them in the past, but they have not been professionally designed.

The website is www.brightholtcare.com.au
I have included a file nook link to use pictures, logo, etc
https://www.filetrove.net/sh/pq3m9tr2x81vbn4/QZXrTy7LmKdNe2Wf-Hpo-4sGj?dl=0

I have included some links to old newsletters, just for the ideas
http://email.pulvio.com.au/em/mail/view.php?id=2004417&a=51290&k=ab91f3e
http://email.pulvio.com.au/em/mail/view.php?id=2003862&a=51290&k=7d2e5c1
http://email.pulvio.com.au/em/mail/view.php?id=2003379&a=51290&k=e40b9a6
http://email.pulvio.com.au/em/mail/view.php?id=2002915&a=51290&k=9c8f174

We are introducing the new cleaning work vehicle and restoration work trailer. The work vehicle which has taken 5 months to build followed by another 5 months to completely fit out with the new custom built machine and equipment is a one of a kind unit, never been attempted before.

We can do a special of 10% off all carpet and upholstery cleaning jobs for the next 30 days, must be booked in the next 14 days to qualify. Including commercial jobs.

Reason: Looking for a unique design and idea. Looking for something fresh. HAVE INCREASED THE BUDGET

Target Market(s)

Everyone and anyone, tenants moving out of rentals, retirees and professionals looking after the home, spring cleans, emergency water and fire damage, mould remeedation, pre sale cleans,

Font styles to use
Sans Serif

Requirements
Must have
• I would like a fresh email newsletter that is informative, one that shows more info each month about the cleaning and restoration industry, offering clients plenty useful info without having to read too much.
• Professional template.
• An email and SMS return message that will make it easy for clients to book in a on site consultation or phone quote.
• A mingleboard add, like section
• and quotation or just a phone call for advice as this is needed for all restoration work.
• Also to find out a bit of info about us and link to the current and any future websites.
Nice to have
• Something new and fresh.
• Links, Visit our website, services, contact us, like us on mingleboard
Should not have
• Surprise me!

```html
<!DOCTYPE html>
<html lang="en">
<head>
<meta charset="utf-8">
<title>Brightholt Care – October 2015 Newsletter</title>
<link href="https://fonts.googleapis.com/css2?family=Open+Sans:wght@300;400;600;700;800&display=swap" rel="stylesheet">
<style>
  :root{
    --navy:#1b3d78;
    --navy-deep:#14295a;
    --pink:#e3197c;
    --pink-deep:#b8125f;
    --teal:#0f5a6b;
    --ink:#333a44;
    --grey:#5a6068;
    --white:#ffffff;
    --paper:#ffffff;
  }
  *{box-sizing:border-box;margin:0;padding:0}
  html,body{width:1200px;height:4000px;overflow:hidden;background:var(--paper)}
  body{font-family:"Open Sans",Arial,sans-serif;color:var(--ink);position:relative}

  .newsletter{position:relative;width:1200px;height:4000px}

  /* Header */
  .masthead{position:absolute;left:0;top:0;width:1200px;height:240px;
    background:linear-gradient(180deg,#234a8c,var(--navy-deep));border-bottom:14px solid var(--pink)}
  .brand{position:absolute;left:40px;top:68px;width:520px;height:90px;display:flex;align-items:center;gap:20px}
  .brand-name{font-weight:700;font-size:46px;color:var(--white);line-height:1;white-space:nowrap}
  .brand-dot{flex:0 0 90px;width:90px;height:90px;border-radius:50%;background:var(--white)}
  .issue{position:absolute;left:610px;top:30px;width:560px;color:var(--white)}
  .issue-date{font-weight:700;font-size:40px;letter-spacing:1px;line-height:1.2}
  .issue-tagline{font-weight:300;font-size:42px;line-height:1.15;margin-top:6px;white-space:nowrap}
  .issue-tagline small{display:block;font-size:27px;margin-top:6px}

  /* Hero offer */
  .hero{position:absolute;left:40px;top:262px;width:1120px;height:496px}
  .hero-photo{position:absolute;top:0;height:496px}
  .hero-photo.left{left:0;width:560px;background:linear-gradient(135deg,#c9d2dc,#7f8fa6 55%,#2e3d5f)}
  .hero-photo.right{left:560px;width:560px;background:linear-gradient(135deg,#e8e9ec,#b9bec6 50%,#8a8f98)}
  .offer-band{position:absolute;left:0;bottom:0;width:1120px;height:118px;background:rgba(27,61,120,.92);
    display:flex;align-items:center;gap:30px;padding-left:20px;color:var(--white)}
  .offer-figure{font-weight:800;font-size:96px;letter-spacing:-2px;line-height:1;white-space:nowrap}
  .offer-text{font-weight:300;font-size:38px;line-height:1.15}
  .offer-terms{position:absolute;left:40px;top:758px;width:1120px;height:50px;background:var(--pink);
    color:var(--white);font-style:italic;font-size:24px;text-align:center;line-height:50px}

  /* Section headings */
  .section-title{position:absolute;left:0;width:1200px;text-align:center;font-weight:300;
    font-size:104px;color:var(--ink);letter-spacing:1px;line-height:1}

  /* Services grid */
  .services{position:absolute;left:40px;top:944px;width:1120px;display:grid;
    grid-template-columns:560px 560px;grid-auto-rows:330px}
  .service{display:flex;align-items:center;padding:0 40px;color:var(--white);font-weight:600;
    font-size:25px;line-height:1.6;text-transform:uppercase}
  .service.blue{background:linear-gradient(135deg,#2b4f96,#163571)}
  .service.pink{background:linear-gradient(135deg,#e7338c,#a8105a)}
  .service.teal{background:linear-gradient(135deg,#1b6a7a,#0b3d4c)}
  .service.pest{grid-column:1 / span 2;justify-content:center;font-size:40px;
    background:linear-gradient(135deg,#c0187a,#7a1a6a 60%,#2a2f70)}

  /* Advice */
  .advice{position:absolute;left:0;top:2630px;width:1200px;text-align:center}
  .advice-label{font-weight:700;font-size:50px;color:var(--ink);letter-spacing:1px}
  .advice-phone{font-weight:800;font-size:78px;color:#1f2328;margin-top:4px}

  /* Social offer */
  .social-offer{position:absolute;left:40px;top:2800px;width:1120px;height:320px;
    background:linear-gradient(180deg,#8fb6dc,#d9dee5 55%,#6c7a88)}
  .social-figure{position:absolute;left:30px;top:40px;font-weight:800;font-size:190px;
    color:var(--pink);line-height:1;letter-spacing:-6px}
  .social-strip{position:absolute;left:0;bottom:0;width:1120px;height:60px;background:rgba(27,61,120,.9);
    color:var(--white);font-size:30px;line-height:60px;padding-left:20px}
  .like-box{position:absolute;right:24px;bottom:14px;width:190px;height:104px;background:var(--navy-deep);
    border:3px solid var(--white);color:var(--white);font-size:22px;padding:10px 14px;line-height:1.3}
  .like-box strong{font-weight:700;font-size:26px;display:block}

  /* About */
  .about-copy{position:absolute;left:40px;top:3296px;width:1120px;font-size:24px;line-height:1.45;color:var(--grey)}
  .about-copy p+p{margin-top:30px}
  .actions{position:absolute;left:40px;top:3680px;width:1120px;height:72px;display:flex}
  .button{flex:1;display:flex;align-items:center;justify-content:center;font-size:34px;
    color:var(--white);text-decoration:none}
  .button.navy{background:var(--navy)}
  .button.pink{background:var(--pink)}

  /* Connect */
  .connect{position:absolute;left:0;top:3908px;width:1200px;display:flex;justify-content:center;gap:60px}
  .connect-item{display:flex;align-items:center;gap:12px;font-size:24px;color:var(--navy);text-decoration:none}
  .connect-dot{width:44px;height:44px;border-radius:50%;background:var(--navy)}
  .connect-dot.pink{background:var(--pink)}
</style>
</head>
<body>
<main class="newsletter">

  <header class="masthead">
    <div class="brand">
      <span class="brand-name">Brightholt Care</span>
      <span class="brand-dot"></span>
    </div>
    <div class="issue">
      <div class="issue-date">OCTOBER 2015</div>
      <div class="issue-tagline">Professional Cleaners
        <small>of Carpets, Rugs, Floors and Fine Fabrics.</small></div>
    </div>
  </header>

  <section class="hero">
    <div class="hero-photo left" role="img" aria-label="Technician cleaning a lounge room carpet with a wand"></div>
    <div class="hero-photo right" role="img" aria-label="Close-up of a tile and grout cleaning machine at work"></div>
    <div class="offer-band">
      <span class="offer-figure">10% OFF</span>
      <span class="offer-text">all carpet and upholstery cleaning jobs<br>for the next 30 days</span>
    </div>
  </section>
  <p class="offer-terms">must be booked in the next 14 days to qualify. Including commercial jobs.</p>

  <h2 class="section-title" style="top:830px">OUR SERVICES</h2>

  <section class="services">
    <div class="service blue">Building inspection &amp;<br>moisture detection</div>
    <div class="service pink">Water damage extraction &amp; drying<br>Building &amp; structural drying<br>Desiccant dehumidification technology drying<br>Contents drying</div>
    <div class="service pink">Mould testing &amp; microbial lab<br>analysis &amp; remediation</div>
    <div class="service teal">Fire &amp; smoke restoration<br>Specialised fire recovery</div>
    <div class="service blue">Premium carpet cleaning,<br>repairs &amp; protection<br>Oriental &amp; area rug cleaning<br>&amp; protection</div>
    <div class="service pink">Upholstery cleaning, repairs<br>&amp; protection<br>Curtain &amp; drapery cleaning</div>
    <div class="service pink">Fabric &amp; fibre protection<br>Leather cleaning &amp; conditioning,<br>repairs &amp; dying<br>Auto and marine carpet &amp;<br>upholstery</div>
    <div class="service teal">Tile &amp; grout cleaning and sealing<br>Natural stone cleaning &amp; sealing<br>Driveway, path &amp; patio cleaning</div>
    <div class="service pest">Pest Control</div>
  </section>

  <section class="advice">
    <div class="advice-label">CALL FOR ADVICE</div>
    <div class="advice-phone">4000 1234 / 0400 555 019</div>
  </section>

  <section class="social-offer" role="img" aria-label="New cleaning work vehicle and restoration trailer parked outdoors">
    <span class="social-figure">10%</span>
    <div class="social-strip">Avail 10% Discount if you like us on mingleboard.</div>
    <div class="like-box">Like us on<strong>mingleboard</strong></div>
  </section>

  <h2 class="section-title" style="top:3170px">ABOUT US</h2>

  <section class="about-copy">
    <p>Stay Dry Carpet Care is one of the original carpet dry cleaning companies established in Harbourton back in the 80's. Back then things were far different but the business was very busy with three vans servicing the motels and homes of Harbourton with portable machinery.</p>
    <p>Darren Whitlow bought Stay Dry Carpet Care in 1995. At that time the focus was on carpet cleaning, upholstery cleaning and area rug cleaning only and the method used was portable hot water extraction. This method involved pre-spraying the carpet or items with a cleaning solution, allowing it to dwell and extracting it while rinsing with a portable machine. We still use this process, in some cases, today. However, we have dramatically increased the steps in this process.</p>
  </section>

  <nav class="actions">
    <a class="button navy" href="https://www.brightholtcare.com.au">Want to Know more about us</a>
    <a class="button pink" href="https://www.brightholtcare.com.au">Go to our Website</a>
  </nav>

  <h2 class="section-title" style="top:3790px;font-size:84px">CONNECT TO US</h2>

  <nav class="connect">
    <a class="connect-item" href="#"><span class="connect-dot"></span>mingleboard</a>
    <a class="connect-item" href="#"><span class="connect-dot"></span>Proflink</a>
    <a class="connect-item" href="#"><span class="connect-dot pink"></span>Clipcast</a>
  </nav>

</main>
</body>
</html>
```